Business Cards for Logistics Company

Looking to update Business Card Design.
Logo is attached. Blue background is not a part of the logo, you can remove it in layers.

Company: Harbor Crest Freightways
Industry: Logistics, Container Shipping

Address:
418 Willow Bend Ave
Bayonne NJ 07419

Phones:
p. 201-555-0143
f. 201-555-0178
c. very by person's name

Website: www.hcfroute.example

Design has to include person's name and position.
OLD Design is included.

B2B

Business

Card Size (non standard): 1039 x 697 pixels, 300dpi
Template is attached.

Font styles to use
Serif
Sans Serif

```html
<!DOCTYPE html>
<html lang="en">
<head>
<meta charset="utf-8">
<title>Harbor Crest Freightways – Business Cards</title>
<link href="https://fonts.googleapis.com/css2?family=PT+Sans:wght@400;700&display=swap" rel="stylesheet">
<style>
  :root {
    --bg: #3a424c;
    --card-dark: #231f20;
    --card-light: #ffffff;
    --brand-blue: #3b78c9;
    --text-grey: #5a5a5a;
    --text-light: #f2f2f2;
  }
  * { margin: 0; padding: 0; box-sizing: border-box; }
  html, body { width: 1200px; height: 960px; overflow: hidden; }
  body {
    background: var(--bg);
    font-family: "PT Sans", Arial, sans-serif;
    display: flex; flex-direction: column; align-items: center; justify-content: center;
    gap: 44px;
  }
  .card {
    position: relative;
    width: 620px; height: 416px;
    border-radius: 26px;
    overflow: hidden;
    box-shadow: 0 8px 24px rgba(0,0,0,.35);
  }
  /* back */
  .card-back { background: var(--card-dark); color: var(--text-light); }
  .brand {
    display: flex; align-items: center; gap: 16px;
  }
  .brand-mark { width: 64px; height: 64px; background: var(--brand-blue); flex: none; }
  .brand-name {
    font-size: 26px; font-weight: 400; letter-spacing: 3px; text-transform: uppercase; line-height: 1.15;
  }
  .card-back .brand { position: absolute; left: 150px; top: 120px; }
  .card-back .brand-name { color: var(--text-light); width: 300px; }
  .tagline {
    position: absolute; left: 0; right: 0; top: 250px; text-align: center;
    color: var(--brand-blue); font-weight: 700; font-size: 15px; letter-spacing: .5px;
  }
  .services {
    position: absolute; left: 0; right: 0; top: 274px; text-align: center;
    font-size: 16px; color: var(--text-light);
  }
  /* front */
  .card-front { background: var(--card-light); }
  .contact { position: absolute; left: 40px; top: 40px; color: var(--text-grey); }
  .person-name { color: var(--brand-blue); font-weight: 700; font-size: 22px; line-height: 1; }
  .person-role { font-size: 15px; margin-top: 2px; }
  .company { color: var(--brand-blue); font-weight: 700; font-size: 15px; margin-top: 16px; }
  .address { font-size: 15px; }
  .lines { list-style: none; margin-top: 12px; font-size: 15px; line-height: 1.4; }
  .lines li { display: flex; align-items: center; gap: 10px; }
  .lines svg { width: 14px; height: 14px; fill: none; stroke: var(--brand-blue); stroke-width: 1.6; }
  .card-front .brand { position: absolute; left: 350px; top: 120px; gap: 12px; }
  .card-front .brand-mark { width: 54px; height: 54px; }
  .card-front .brand-name { color: var(--brand-blue); font-size: 20px; width: 210px; }
  .swoosh { position: absolute; left: 0; top: 0; width: 620px; height: 416px; }
  .website {
    position: absolute; right: 120px; bottom: 30px;
    color: var(--text-light); font-size: 17px;
  }
</style>
</head>
<body>

  <section class="card card-back">
    <div class="brand">
      <span class="brand-mark"></span>
      <span class="brand-name">Harbor Crest Freightways</span>
    </div>
    <p class="tagline">INTERNATIONAL TRANSPORTATION SOLUTIONS</p>
    <p class="services">Ocean &amp; Air Freight &nbsp;•&nbsp; Loading &amp; Storage &nbsp;•&nbsp; Multimodal Transport</p>
  </section>

  <section class="card card-front">
    <svg class="swoosh" viewBox="0 0 620 416" aria-hidden="true">
      <path d="M0 262 Q60 250 180 268 Q420 305 620 390 L620 416 L0 416 Z" fill="var(--brand-blue)"/>
      <path d="M0 268 Q60 258 180 276 Q420 314 620 402 L620 416 L0 416 Z" fill="var(--card-dark)"/>
    </svg>
    <div class="contact">
      <p class="person-name">Dmitri Valenko</p>
      <p class="person-role">General Manager</p>
      <p class="company">Harbor Crest Freightways</p>
      <p class="address">418 Willow Bend Ave, Bayonne NJ 07419</p>
      <ul class="lines">
        <li><svg viewBox="0 0 14 14"><path d="M2 4 Q7 0 12 4 L11 6 L9 5 L9 4 Q7 3 5 4 L5 5 L3 6 Z M3 8 H11 V12 H3 Z"/></svg>201-555-0143</li>
        <li><svg viewBox="0 0 14 14"><rect x="4" y="1.5" width="6" height="4"/><rect x="1.5" y="5.5" width="11" height="5"/><rect x="4" y="9" width="6" height="3.5"/></svg>201-555-0178</li>
        <li><svg viewBox="0 0 14 14"><rect x="3.5" y="1" width="7" height="12" rx="1.2"/><path d="M6 11 H8"/></svg>646-555-0192</li>
        <li><svg viewBox="0 0 14 14"><rect x="1" y="3" width="12" height="8"/><path d="M1 3 L7 8 L13 3"/></svg>info@hcfroute.example</li>
      </ul>
    </div>
    <div class="brand">
      <span class="brand-mark"></span>
      <span class="brand-name">Harbor Crest Freightways</span>
    </div>
    <p class="website">www.hcfroute.example</p>
  </section>

</body>
</html>
```